Business Card Design Project

We are looking for an eye catching, unique business card design that incorporates our logo and a photo of the mortgage associate.

We will need to have our business address included (could be on the back of the card), as well as the mortgage associate's information:

Name
Position
Phone
Email

Logo attached.

Target Market(s)

Clients (people purchasing homes, renewing existing mortgages, or refinancing existing mortgages)
Referral sources such as realtors, financial advisors, relocation specialists, real estate lawyers...

Industry/Entity Type

Business

Requirements
Must have
• Logo
Name and contact information of associate
Address of brokerage
Nice to have
• Photo of the agent

```html
<!DOCTYPE html>
<html lang="en">
<head>
<meta charset="utf-8">
<title>Keystone Lending Group – Business Card</title>
<link href="https://fonts.googleapis.com/css2?family=Montserrat:wght@500;800&family=Noto+Serif&family=Open+Sans:wght@400;600&display=swap" rel="stylesheet">
<style>
  :root {
    --backdrop: #d9d9d9;
    --brand-red: #9b1b1f;
    --ink-dark: #2a2a2a;
    --ink-grey: #555555;
    --card-white: #f7f8f8;
    --social-blue: #5b7fbf;
    --photo-light: #eef2f6;
    --photo-mid: #a9b8cc;
    --photo-deep: #5f7696;
  }
  * { box-sizing: border-box; margin: 0; padding: 0; }
  html, body { width: 1200px; height: 900px; overflow: hidden; }
  body {
    background: var(--backdrop);
    display: flex;
    flex-direction: column;
    align-items: center;
    justify-content: center;
    gap: 40px;
  }
  .card {
    width: 680px;
    height: 389px;
    position: relative;
    overflow: hidden;
  }

  /* Front side */
  .card-front { display: flex; background: var(--brand-red); }
  .front-brand {
    width: 55%;
    display: flex;
    flex-direction: column;
    justify-content: center;
    padding: 0 40px;
    color: #ffffff;
  }
  .front-brand .brand-name {
    font-family: "Montserrat", sans-serif;
    font-weight: 800;
    font-size: 31px;
    line-height: 1.1;
    letter-spacing: 0.5px;
    text-transform: uppercase;
  }
  .front-brand .tagline {
    font-family: "Montserrat", sans-serif;
    font-weight: 500;
    font-size: 12px;
    letter-spacing: 0.8px;
    margin-top: 16px;
    white-space: nowrap;
  }
  .front-photo {
    width: 45%;
    height: 100%;
    background: radial-gradient(circle at 55% 40%, var(--photo-light) 0%, var(--photo-mid) 55%, var(--photo-deep) 100%);
  }

  /* Back side */
  .card-back {
    background: var(--card-white);
    padding: 48px 44px 40px 44px;
  }
  .back-brand {
    font-family: "Montserrat", sans-serif;
    font-weight: 800;
    font-size: 30px;
    line-height: 1.1;
    color: var(--ink-dark);
    text-transform: uppercase;
    letter-spacing: 0.5px;
  }
  .associate {
    position: absolute;
    left: 44px;
    bottom: 92px;
  }
  .associate-name {
    font-family: "Noto Serif", serif;
    font-size: 26px;
    color: var(--brand-red);
  }
  .associate-role {
    font-family: "Open Sans", sans-serif;
    font-size: 15px;
    color: var(--ink-grey);
    margin-top: 4px;
  }
  .contact {
    position: absolute;
    right: 44px;
    bottom: 52px;
    text-align: right;
    font-family: "Open Sans", sans-serif;
    font-style: normal;
    font-size: 15px;
    line-height: 1.4;
    color: var(--ink-grey);
  }
  .social {
    display: flex;
    justify-content: flex-end;
    gap: 8px;
    margin-top: 8px;
  }
</style>
</head>
<body>
  <section class="card card-front">
    <div class="front-brand">
      <div class="brand-name">Keystone<br>Lending Group</div>
      <p class="tagline">Home loans shaped around the way you live</p>
    </div>
    <div class="front-photo" role="img" aria-label="Photo of a hand holding out a house key with a small house-shaped key ring"></div>
  </section>

  <section class="card card-back">
    <div class="back-brand">Keystone<br>Lending Group</div>

    <div class="associate">
      <p class="associate-name">Mara Ellison</p>
      <p class="associate-role">General Manager</p>
    </div>

    <address class="contact">
      48 Alder Lane<br>
      Brookfield, ON 40219<br>
      (555) 014 2290<br>
      mellison@keystonelending.com
      <span class="social">
        <svg width="20" height="20" viewBox="0 0 20 20" aria-label="Social profile"><circle cx="10" cy="10" r="10" fill="var(--social-blue)"/></svg>
        <svg width="20" height="20" viewBox="0 0 20 20" aria-label="Social profile"><circle cx="10" cy="10" r="10" fill="var(--social-blue)"/></svg>
      </span>
    </address>
  </section>
</body>
</html>
```